An eCommerce Business Needs a Wordpress Web Design and Development

We need a website design and development for a new eCommerce business based in New York called "Velvet Ondra". We sell items that are based on satisfying multi-sensory pathways of the person, as we believe that all is interconnected forming the Universal Language. All our products are made of raw natural elements from earth or the cosmos. The final design should communicate visual-perceptive pathways that produce harmonious effects and creativity.
Updates

Dear Designers, Please accept my sincere apology for my delayed response. I am currently in the midst of extensive business travelling while at the same time gathering feedback from online polling with friends as the website potential end-users. I shall get back to you by May 12 or sooner. Thank you for your understanding.

Target Market(s)

Art, fossils, minerals and numismatic collectors.

Industry/Entity Type

Online Shopping

Coding

Coded - Design and coding required

Number of Pages Required

5+ page

Font styles to use
Sans Serif
Script

Colors

Designer to choose colors to be used in the design.

Requirements
Must have
• - Simple and clean design.
• - Desktop and mobile device friendly.
• - Photos and images of string musical instruments, crystals, numismatics and cultural artefacts.
• - A blog page.
• - A check-out cart for online shopping and payment. Example: https://shop.pelmora-example.com
• - Standard links to social media.

```html
<!DOCTYPE html>
<html lang="en">
<head>
<meta charset="utf-8">
<title>Velvet Ondra — Home</title>
<link rel="stylesheet" href="https://fonts.googleapis.com/css2?family=Open+Sans:wght@400;600;700&family=Zilla+Slab:wght@400;500;600&display=swap">
<style>
:root{
  --gold:#a8913a;
  --gold-light:#c9b56a;
  --navy:#123f74;
  --navy-deep:#07386c;
  --teal:#5dd3d3;
  --teal-deep:#35b8b8;
  --ink:#333;
  --muted:#666;
  --white:#fff;
  --footer-bar:#e9e4cf;
  --line:#d9d9d9;
}
*{box-sizing:border-box;margin:0;padding:0}
html,body{width:1200px;height:3267px;overflow:hidden}
body{position:relative;background:var(--white);font-family:"Open Sans",Arial,sans-serif;color:var(--ink)}
.abs{position:absolute}
.slab{font-family:"Zilla Slab",Georgia,serif}

/* top bar */
.topbar{left:0;top:0;width:1200px;height:35px;background:var(--gold);color:var(--white);font-size:12px;font-weight:600;letter-spacing:.3px}
.topbar span{position:absolute;top:9px;display:flex;align-items:center;gap:6px}
.topbar svg{width:14px;height:14px}

/* header */
.header{left:0;top:35px;width:1200px;height:105px;background:var(--white)}
.logo{left:120px;top:11px;width:162px;height:162px;border-radius:50%;background:var(--white);border:2px dotted var(--gold);z-index:5;display:flex;align-items:center;justify-content:center;text-align:center}
.logo-name{font-family:"Zilla Slab",Georgia,serif;font-weight:600;font-size:27px;line-height:1.05;color:var(--navy);letter-spacing:1px}
.nav{top:35px;left:0;height:105px;width:1200px}
.nav a{position:absolute;top:42px;font-size:15px;color:var(--navy);text-decoration:none;letter-spacing:.3px}
.nav .home{left:368px;top:14px;width:80px;height:80px;border-radius:50%;border:2px dotted var(--line);display:flex;align-items:center;justify-content:center;color:var(--gold)}
.cart{left:994px;top:40px;color:var(--gold);font-size:15px;display:flex;gap:6px;align-items:center}

/* hero */
.hero{left:0;top:140px;width:1200px;height:562px;background:linear-gradient(90deg,#5ed6d4 0%,#6fdcd9 60%,#7fe2df 100%);overflow:hidden}
.hero-photo{left:0;top:30px;width:560px;height:500px;background:radial-gradient(ellipse at 40% 60%,#b5743a 0%,#7a4a22 35%,rgba(90,60,30,0) 70%)}
.hero-floor{left:0;top:450px;width:1200px;height:112px;background:linear-gradient(180deg,#c89a6b,#e6d2bd 60%,#f2f2f2)}
.hero-ring{left:698px;top:55px;width:360px;height:360px;border-radius:50%;border:3px dotted var(--white)}
.hero-disc{left:730px;top:87px;width:296px;height:296px;border-radius:50%;background:var(--teal-deep);text-align:center;color:var(--white);padding-top:68px}
.hero-disc h1{font-family:"Zilla Slab",Georgia,serif;font-weight:400;font-size:36px;line-height:1.05}
.hero-disc p{font-size:14px;line-height:1.5;margin:14px auto 0;width:250px}
.btn-gold{display:inline-block;background:var(--gold);color:var(--white);font-size:14px;font-weight:600;border-radius:20px;padding:10px 28px;margin-top:20px}
.dot{width:34px;height:34px;border-radius:50%;background:var(--white)}
.arrow{width:30px;height:50px}
.band-thin{left:0;top:697px;width:1200px;height:8px;background:#dbeef5}

/* products */
.section-title{width:1200px;left:0;text-align:center;font-family:"Zilla Slab",Georgia,serif;font-size:31px;color:var(--navy);font-weight:500}
.tile{top:828px;width:229px;height:287px;overflow:hidden}
.tile .cap{position:absolute;left:0;bottom:24px;width:100%;height:56px;background:rgba(18,63,116,.85);color:var(--white);font-family:"Zilla Slab",Georgia,serif;font-size:19px;line-height:1;display:flex;align-items:center;justify-content:center;text-align:center}
.tile.gold .cap{background:rgba(168,145,58,.85)}

/* about */
.about{left:0;top:1194px;width:1200px;height:492px;background:var(--navy-deep)}
.about-photo{left:0;top:0;width:760px;height:492px;clip-path:polygon(0 0,760px 0,620px 246px,720px 492px,0 492px);background:linear-gradient(120deg,#1a1a1a 0%,#3c2418 30%,#a4501f 50%,#d8d8d8 75%,#222 100%)}
.about-text{left:743px;top:104px;width:360px;color:var(--white)}
.about-text h2{font-family:"Zilla Slab",Georgia,serif;font-weight:500;font-size:31px;line-height:1.05}
.about-text p{font-size:13px;line-height:1.62;margin-top:16px;color:#dfe7f1}
.btn-outline{display:inline-block;border:2px solid var(--white);border-radius:24px;padding:10px 30px;font-size:14px;font-weight:600;margin-top:24px}

/* featured */
.product{top:1808px;width:240px}
.product .img{height:272px;width:200px}
.product h3{font-family:"Zilla Slab",Georgia,serif;font-size:17px;font-weight:600;color:var(--ink);margin-top:38px}
.product .desc{font-size:11px;color:var(--muted);margin-top:6px}
.product .row{display:flex;align-items:center;gap:40px;margin-top:14px}
.price{font-size:24px;color:var(--navy)}
.stars{color:var(--gold);font-size:16px;letter-spacing:1px}
.buy{display:inline-block;margin-top:12px;width:131px;height:34px;border:2px solid var(--gold);border-radius:18px;text-align:center;line-height:30px;font-size:11px;font-weight:700;color:var(--navy)}
.pager{left:540px;top:2278px;display:flex;gap:6px;align-items:center}
.pager i{display:block;width:9px;height:9px;border-radius:50%;background:#ccc}
.pager b{display:block;width:18px;height:18px;border-radius:50%;background:#999}

/* discount */
.promo{left:0;top:2352px;width:1200px;height:518px;background:linear-gradient(180deg,#1f78d4 0%,#4f9ae2 30%,#9bc8f0 65%,#dfeefb 100%)}
.promo-text{left:140px;top:150px;color:var(--ink)}
.promo-text h2{font-family:"Zilla Slab",Georgia,serif;font-weight:500;font-size:37px;line-height:1.1;color:#111}
.promo-text h3{font-family:"Zilla Slab",Georgia,serif;font-weight:500;font-size:27px;color:#111;margin-top:4px}
.promo-text p{font-size:14px;line-height:1.6;width:360px;margin-top:16px}
.promo-art{left:562px;top:88px;width:462px;height:337px;background:radial-gradient(ellipse at 30% 55%,#a0603a 0%,rgba(160,96,58,.6) 25%,rgba(160,96,58,0) 45%),radial-gradient(ellipse at 72% 50%,#b57a52 0%,rgba(181,122,82,.6) 30%,rgba(181,122,82,0) 55%)}

/* footer */
.footer{left:0;top:2870px;width:1200px;height:332px}
.fcol{top:80px}
.fcol h4{font-family:"Zilla Slab",Georgia,serif;font-size:18px;font-weight:600;color:var(--navy);margin-bottom:20px}
.fcol li{list-style:none;font-size:14px;color:var(--ink);line-height:30px}
.email{width:276px;height:40px;border:1px solid #aaa;border-radius:20px;padding-left:22px;font-size:14px;line-height:38px;color:var(--muted)}
.subscribe{display:inline-block;background:var(--gold);color:var(--white);border-radius:18px;padding:7px 28px;font-size:15px;margin-top:10px}
.social{display:flex;gap:8px;margin-top:14px}
.social span{width:36px;height:36px;border-radius:50%;border:2px solid var(--navy)}
.contact-line{display:flex;gap:8px;align-items:center;font-size:14px;line-height:32px}
.cards{display:flex;gap:6px;margin-top:14px}
.cards span{width:35px;height:23px;border-radius:3px;background:#5b7dbb}
.bottom{left:0;top:3202px;width:1200px;height:65px;background:var(--footer-bar);text-align:center;font-size:12px;line-height:65px;color:#555}
</style>
</head>
<body>

<div class="abs topbar">
  <span style="left:333px"><svg viewBox="0 0 16 16" fill="none" stroke="#fff" stroke-width="2"><circle cx="7" cy="7" r="5"/><path d="M11 11l4 4"/></svg>SEARCH HERE</span>
  <span style="left:628px"><svg viewBox="0 0 16 16" fill="#fff"><path d="M3 1l3 3-2 2c1 2 3 4 5 5l2-2 3 3-2 3C7 15 1 9 1 3z"/></svg>CALL US TODAY: 555-014-2260</span>
  <span style="left:862px">LOGIN &nbsp;|&nbsp; REGISTER &nbsp;|&nbsp; MY ACCOUNT</span>
</div>

<header class="abs header"></header>
<div class="abs logo"><div class="logo-name">VELVET<br>ONDRA</div></div>
<nav class="abs nav">
  <a class="home">HOME</a>
  <a style="left:466px">ABOUT US</a>
  <a style="left:580px">OUR PRODUCTS</a>
  <a style="left:736px">SHOP NOW</a>
  <a style="left:858px">CONTACT US</a>
</nav>
<div class="abs cart" style="top:75px"><svg width="26" height="22" viewBox="0 0 26 22" fill="none" stroke="#123f74" stroke-width="2"><path d="M1 6h24l-3 13H4z"/><path d="M8 6l4-5M18 6l-4-5"/></svg>0 ITEMS</div>

<section class="abs hero">
  <div class="abs hero-photo" role="img" aria-label="Guitars, saxophone and violin standing against a turquoise wall"></div>
  <div class="abs hero-floor"></div>
  <div class="abs hero-ring"></div>
  <div class="abs dot" style="left:860px;top:38px"></div>
  <div class="abs dot" style="left:860px;top:398px"></div>
  <div class="abs dot" style="left:681px;top:218px"></div>
  <div class="abs dot" style="left:1036px;top:218px"></div>
  <div class="abs hero-disc">
    <h1>BEST MUSICAL<br>INSTRUMENTS</h1>
    <p>Our guitars and other musical instruments would satisfy your auditory,</p>
    <span class="btn-gold">SHOP NOW</span>
  </div>
  <svg class="abs arrow" style="left:86px;top:205px" viewBox="0 0 30 50" fill="none" stroke="#fff" stroke-width="3"><path d="M24 3L5 25l19 22"/></svg>
  <svg class="abs arrow" style="left:1110px;top:205px" viewBox="0 0 30 50" fill="none" stroke="#fff" stroke-width="3"><path d="M6 3l19 22L6 47"/></svg>
</section>
<div class="abs band-thin"></div>

<h2 class="abs section-title" style="top:760px">OUR PRODUCTS</h2>
<div class="abs tile gold" style="left:122px;background:linear-gradient(160deg,#3a2a20,#8a4a22 60%,#2a1c14)" role="img" aria-label="Violin and flute on a dark table">
  <div class="cap">MUSICAL<br>INSTRUMENTS</div></div>
<div class="abs tile" style="left:366px;background:linear-gradient(160deg,#5a1f7a,#9c4fc0 50%,#4a1860)" role="img" aria-label="Purple amethyst crystal close-up">
  <div class="cap">CRYSTALS</div></div>
<div class="abs tile" style="left:612px;background:radial-gradient(circle at 55% 45%,#cfcabc,#8a867c 55%,#3c3a34)" role="img" aria-label="Silver antique coin">
  <div class="cap">NUMISMATIC<br>COLLECTIBLES</div></div>
<div class="abs tile" style="left:856px;background:radial-gradient(circle at 50% 40%,#b88f68,#7a5536 60%,#3e2c1e)" role="img" aria-label="Carved stone cultural artifact">
  <div class="cap">CULTURAL<br>ARTIFACTS</div></div>

<section class="abs about">
  <div class="abs about-photo" role="img" aria-label="Violin resting on piano keys"></div>
  <div class="abs about-text">
    <h2>ABOUT<br>VELVET ONDRA</h2>
    <p>Velvet Ondra is a dedicated company, which foundation is based on an integrative view of the Universe. We seek items from all over the world, carefully selected to meet high standards of our merchandise. We sell items that are based on satisfying multi-sensory pathways of the person, as we believe that all is interconnected forming the Universal Language.</p>
    <span class="btn-outline">READ MORE</span>
  </div>
</section>

<h2 class="abs section-title" style="top:1745px">FEATURED PRODUCTS</h2>
<div class="abs product" style="left:126px">
  <div class="img" style="background:radial-gradient(ellipse at 45% 50%,#c8b0d8,#e6dcec 45%,#fff 70%)" role="img" aria-label="Pale amethyst crystal cluster"></div>
  <h3>PRODUCTS NAME</h3><div class="desc">Etiam eu urna Sed porta Suspen</div>
  <div class="row"><span class="price">$120</span><span class="stars">★★★★★</span></div>
  <span class="buy">BUY NOW</span>
</div>
<div class="abs product" style="left:390px">
  <div class="img" style="background:radial-gradient(ellipse 22% 48% at 35% 50%,#8a3c18,#b8642c 50%,#fff 100%)" role="img" aria-label="Violin standing upright"></div>
  <h3>PRODUCTS NAME</h3><div class="desc">Etiam eu urna Sed porta Suspen</div>
  <div class="row"><span class="price">$120</span><span class="stars">★★★★★</span></div>
  <span class="buy">BUY NOW</span>
</div>
<div class="abs product" style="left:638px">
  <div class="img" style="background:radial-gradient(ellipse 28% 46% at 40% 50%,#b8602e,#d48a5a 55%,#fff 100%)" role="img" aria-label="Ancient terracotta amphora"></div>
  <h3>PRODUCTS NAME</h3><div class="desc">Etiam eu urna Sed porta Suspen</div>
  <div class="row"><span class="price">$120</span><span class="stars">★★★★★</span></div>
  <span class="buy">BUY NOW</span>
</div>
<div class="abs product" style="left:900px">
  <div class="img" style="background:radial-gradient(circle at 36% 50%,#9a968a,#6a675e 28%,#fff 34%)" role="img" aria-label="Antique silver coin"></div>
  <h3>PRODUCTS NAME</h3><div class="desc">Etiam eu urna Sed porta Suspen</div>
  <div class="row"><span class="price">$120</span><span class="stars">★★★★★</span></div>
  <span class="buy">BUY NOW</span>
</div>
<div class="abs pager"><b></b><i style="background:#888"></i><i></i><i></i><i></i><b></b></div>

<section class="abs promo">
  <div class="abs promo-art" role="img" aria-label="Ancient chalice and sphinx statue against the sky"></div>
  <div class="abs promo-text">
    <h2>GET 25%<br>DISCOUNT NOW</h2>
    <h3>ON YOUR FIRST PURCHASE</h3>
    <p>Vivamus porttitor purus nisi eleifend libero a tempus libero lectus feugiat felis Morbi diam mauris</p>
    <span class="btn-gold" style="margin-top:34px;padding:11px 32px">SHOP NOW</span>
  </div>
</section>

<footer class="abs footer">
  <div class="abs fcol" style="left:122px">
    <h4>SIGN UP NEWSLETTERS</h4>
    <div class="email">Email address</div>
    <span class="subscribe">Subscribe</span>
    <div class="social"><span aria-label="Social link"></span><span aria-label="Social link"></span><span aria-label="Social link"></span><span aria-label="Social link"></span></div>
  </div>
  <div class="abs fcol" style="left:460px">
    <h4>QUICK LINKS</h4>
    <ul><li>Home</li><li>About Us</li><li>Products</li><li>Shop Now</li></ul>
  </div>
  <div class="abs fcol" style="left:658px">
    <h4>RESOURCES</h4>
    <ul><li>My Account</li><li>My Cart</li><li>Register</li><li>Log In</li></ul>
  </div>
  <div class="abs fcol" style="left:852px">
    <h4>CONTACT US</h4>
    <div class="contact-line"><svg width="18" height="18" viewBox="0 0 16 16" fill="none" stroke="#123f74" stroke-width="1.5"><path d="M3 1l3 3-2 2c1 2 3 4 5 5l2-2 3 3-2 3C7 15 1 9 1 3z"/></svg>555.014.2261</div>
    <div class="contact-line"><svg width="18" height="14" viewBox="0 0 18 14" fill="none" stroke="#123f74" stroke-width="1.5"><rect x="1" y="1" width="16" height="12"/><path d="M1 1l8 7 8-7"/></svg>info@velvetondra-example.com</div>
    <div class="cards"><span></span><span></span><span></span><span></span><span></span></div>
  </div>
</footer>
<div class="abs bottom">© 2018 Company Name &nbsp;All right reserved</div>

</body>
</html>
```